New Logo, New Business Cards! Looking for Refresh

We're in the process of modernizing our entire organization, and with that came the redesign of our logo (attached). We're looking for a designer to develop our new business cards.
Looking for a design that will bring the company in 2020 and help showcase our new logo. Work with the colors of the logo. Feel free to experiment with the logo in white or black if you want. Both now attached.
Industry/Entity Type
Non Profit
Contact Information for Business Card
Address:
48315 Brackwell Avenue, Suite 512
Richmond Hill, ON, L7R 5K2
Name: Marcus Delvecki, MBA
Position: Executive Director
Telephone: 905-362-7048, Ext. 218
Cell Phone: 416-573-2046
Email: marcus@quorvel.ca
Website: www.quorvel.ca
Look and feel
Each slider illustrates characteristics of the customer's brand and the style your logo design should communicate.

```html
<!DOCTYPE html>
<html lang="en">
<head>
<meta charset="utf-8">
<title>Quorvel Business Card</title>
<link rel="stylesheet" href="https://fonts.googleapis.com/css2?family=Montserrat:wght@400;500;700;800&display=swap">
<style>
  :root {
    --backdrop: #5b4f46;
    --card-dark: #242424;
    --card-light: #f4f4f4;
    --brand-white: #f1f1f1;
    --green-dark: #1d4a2a;
    --green: #3f9a3c;
    --red: #d42020;
    --ink: #2b2b2b;
  }
  * { margin: 0; padding: 0; box-sizing: border-box; }
  html, body {
    width: 1200px; height: 1200px; overflow: hidden;
    background: var(--backdrop);
    font-family: "Montserrat", sans-serif;
  }
  .card {
    position: absolute; left: 180px; width: 840px; height: 480px;
    box-shadow: 0 6px 18px rgba(0,0,0,.45);
  }
  .card-front {
    top: 96px;
    background: var(--card-dark);
    display: flex; align-items: center; justify-content: center;
  }
  .pattern-area { position: absolute; inset: 0; background: radial-gradient(circle at 50% 50%, #2c2c2c, #222 75%); }
  .brand-mark {
    position: relative; display: flex; align-items: center; gap: 18px;
    font-weight: 800; letter-spacing: 4px; line-height: 1;
  }
  .brand-mark .brand-square { display: block; background: currentColor; }
  .card-front .brand-mark { color: var(--brand-white); font-size: 96px; }
  .card-front .brand-square { width: 60px; height: 60px; }

  .card-back { top: 616px; background: var(--card-light); }
  .card-back .brand-mark {
    position: absolute; top: 52px; right: 40px;
    color: var(--green-dark); font-size: 62px; gap: 12px;
  }
  .card-back .brand-square { width: 40px; height: 40px; }

  .person { position: absolute; left: 40px; top: 222px; }
  .person-name { font-size: 28px; font-weight: 700; color: var(--green-dark); }
  .person-name .credential { color: var(--green); }
  .person-title { margin-top: 8px; font-size: 19px; color: var(--red); }

  .divider { position: absolute; left: 40px; right: 40px; top: 308px; height: 3px; background: var(--green); }

  .contact-list { position: absolute; left: 40px; top: 326px; list-style: none; }
  .contact-list li {
    display: flex; align-items: center; gap: 8px;
    font-size: 21px; color: var(--ink); height: 30.5px;
  }
  .contact-list svg { width: 20px; height: 20px; fill: var(--green); flex: none; }

  .address {
    position: absolute; right: 40px; top: 346px; text-align: right;
    font-style: normal; font-size: 21px; color: var(--ink); line-height: 33px;
  }
</style>
</head>
<body>
  <section class="card card-front">
    <div class="pattern-area" role="img" aria-label="Repeating pattern of faint maple leaves on charcoal"></div>
    <div class="brand-mark"><span class="brand-square"></span>QUORVEL</div>
  </section>

  <section class="card card-back">
    <div class="brand-mark"><span class="brand-square"></span>QUORVEL</div>

    <div class="person">
      <h1 class="person-name">Marcus Delvecki<span class="credential">, MBA</span></h1>
      <p class="person-title">Executive Director</p>
    </div>

    <div class="divider"></div>

    <ul class="contact-list">
      <li><svg viewBox="0 0 20 20"><path d="M6 1h8a1.5 1.5 0 0 1 1.5 1.5v15A1.5 1.5 0 0 1 14 19H6a1.5 1.5 0 0 1-1.5-1.5v-15A1.5 1.5 0 0 1 6 1zm0 2v12h8V3zm4 13a1 1 0 1 0 0 2 1 1 0 0 0 0-2z"/></svg>416-573-2046</li>
      <li><svg viewBox="0 0 20 20"><path d="M2 7c0-2 3-4 8-4s8 2 8 4v2h-4V7.5c-1-.5-2.5-.8-4-.8s-3 .3-4 .8V9H2zm3 3h10l3 5v3H2v-3zm5 1.5a2.5 2.5 0 1 0 0 5 2.5 2.5 0 0 0 0-5z"/></svg>905-362-7048, Ext. 218</li>
      <li><svg viewBox="0 0 20 20"><path d="M1 4h18v12H1zm2 2v.5l7 5 7-5V6l-7 5z"/></svg>marcus@quorvel.ca</li>
      <li><svg viewBox="0 0 20 20"><path d="M10 1a9 9 0 1 0 0 18 9 9 0 0 0 0-18zm-1 2.5c-1 1-1.5 2.5-3 3s-2 2-1 3.5 3 1 3.5 2.5-1 3-.5 4A7 7 0 0 1 3.5 8 7 7 0 0 1 9 3.5zm3 .3a7 7 0 0 1 4.7 9.4c-.7-.8-1.7-1-2.2-2s.5-2-.5-3-2.5 0-3-1.2.5-2.2 1-3.2z"/></svg>www.quorvel.ca</li>
    </ul>

    <address class="address">
      48315 Brackwell Avenue<br>
      Suite 512<br>
      Richmond Hill, ON, L7R 5K2
    </address>
  </section>
</body>
</html>
```